Web Design for an Online Dating Web Site

We need an uncoded web design for a new online dating web site called pLirvo.com. Simplicity and boldness are the key factors in the successful design.
Please look at the requirements document attached for details.
Updates
Dear all,
Please AVOID USING A PICTURE OF A HAPPY COUPLE ON THE HOME PAGE of the site. We highly want to move away from this space as it makes our web site just like another dating web site.
We like something simple with web 2.0 look and feel. The examples in the Requirements Document are exactly the design we are after.
Regards
Tarn
Industry/Entity Type
Dating
Look and feel
Each slider illustrates characteristics of the customer's brand and the style your logo design should communicate.

```html
<!DOCTYPE html>
<html lang="en">
<head>
<meta charset="utf-8">
<title>pLirvo.com — Successful Dating with Professional Dating Advice</title>
<link href="https://fonts.googleapis.com/css2?family=Arimo:wght@400;700&display=swap" rel="stylesheet">
<style>
:root{
  --dark:#3f3f3b;
  --darker:#2c2c2a;
  --header:#ffffff;
  --page:#e9e9e7;
  --ink:#222;
  --grey:#4a4a4a;
  --blue:#1b86b3;
  --green:#7cbf2b;
  --green-dark:#5e9d17;
  --field:#dcdcda;
  --field-dark:#141414;
  --c-blue:#5793c8;--c-teal:#77cfc7;--c-purple:#9583cf;--c-orange:#f5a11b;--c-green:#86c340;
}
*{margin:0;padding:0;box-sizing:border-box}
html,body{width:862px;height:1200px;overflow:hidden}
body{position:relative;background:var(--page);font-family:'Arimo',Arial,sans-serif;color:var(--ink)}
.abs{position:absolute}
.topbar{left:0;top:0;width:862px;height:32px;background:var(--dark)}
.share{top:5px;width:22px;height:22px;background:#8a8a88;border-radius:3px}
.header{left:0;top:32px;width:862px;height:131px;background:var(--header)}
.brand{left:98px;top:44px;font-size:50px;font-weight:700;color:#7a7a78;letter-spacing:-1px;display:flex;align-items:center;gap:10px}
.brand i{display:block;width:26px;height:26px;border-radius:50%;background:var(--green)}
.nav{left:458px;top:40px;width:318px;height:46px;border-radius:20px 0 0 20px;background:linear-gradient(#fff,#f1f1f0);box-shadow:0 2px 4px rgba(0,0,0,.08)}
.nav a{position:absolute;top:13px;font-size:12px;color:#444;text-decoration:none}
.nav .active{left:41px;top:7px;width:64px;height:24px;border-radius:12px;background:linear-gradient(#9dd456,var(--green));color:#fff;text-align:center;line-height:24px}
.login label{position:absolute;font-size:9px;color:#333}
.login .field{position:absolute;left:541px;width:105px;height:18px;background:var(--field);border:1px solid #c8c8c6;border-radius:3px;font-size:8px;color:#555;padding:4px 6px}
.login .btn{left:652px;top:92px;width:46px;height:32px;background:linear-gradient(#9dd456,var(--green-dark));color:#fff;font-size:14px;text-align:center;line-height:32px;border-radius:3px}
h1{left:97px;top:186px;font-size:47px;font-weight:700;line-height:50px;color:var(--grey);letter-spacing:.3px}
h1 span,.lead span,.join,.popular h2{color:var(--blue)}
.lead{left:98px;top:294px;font-size:13px;color:#333}
.post{left:96px;width:440px}
.post .mark{position:absolute;left:0;top:0;width:40px;height:37px;border-radius:3px;color:#fff;font-size:24px;font-weight:700;text-align:center;line-height:37px}
.post .meta{position:absolute;left:48px;top:0;font-size:8px;color:#333;white-space:nowrap}
.post .meta b{font-weight:400}
.post p{position:absolute;left:48px;top:13px;width:400px;font-size:9px;line-height:13px;color:#333;white-space:nowrap}
.popular h2{left:97px;top:667px;font-size:19px;font-weight:400}
.popular ul{left:98px;top:697px;list-style:none;width:300px}
.popular li{position:absolute;left:0;font-size:9px;font-weight:700;width:300px;line-height:13px}
.popular li::before{content:"";position:absolute;left:0;top:4px;width:3px;height:3px;background:#333}
.popular li span{display:block;padding-left:11px}
.popular li small{display:block;padding-left:11px;font-weight:400;font-size:8px;margin-top:1px}
.join{left:574px;top:333px;font-size:22px;font-weight:700}
.input{left:573px;width:203px;height:26px;background:var(--field);border-radius:3px;font-size:9px;color:#aaa;padding:8px 14px}
.signup{left:574px;top:476px;width:110px;height:28px;background:linear-gradient(#93cf4c,var(--green));color:#fff;font-size:19px;padding-left:10px;line-height:28px;border-radius:2px}
.why{left:574px;top:514px;font-size:20px;font-weight:700;color:#222}
.why span{color:var(--green)}
.why small{display:block;font-size:13px;margin-top:4px}
.feature{left:574px;width:215px;font-size:7.5px;font-weight:700;line-height:11px;padding-left:19px;white-space:nowrap}
.feature i{position:absolute;left:0;top:1px;width:14px;height:14px;border-radius:2px}
.cta{left:574px;top:654px;width:83px;height:26px;background:linear-gradient(#3aa3d9,#1674a8);color:#fff;font-size:10px;font-weight:700;text-align:center;line-height:26px;border-radius:4px}
.video-label{left:574px;top:763px;font-size:13px}
.footer{left:0;top:895px;width:862px;height:285px;background:var(--dark)}
.fbrand{left:98px;top:930px;font-size:34px;font-weight:700;color:#6e6e6a;display:flex;align-items:center;gap:8px}
.fbrand i{display:block;width:16px;height:16px;border-radius:50%;background:#6e6e6a}
.contact{left:98px;color:#fff;font-size:10px;padding-left:27px}
.contact h3{font-size:14px;color:var(--green);margin-bottom:5px}
.contact p{line-height:17px}
.contact svg{position:absolute;left:0;top:0}
.flinks{left:300px;top:982px;list-style:none}
.flinks li{font-size:10px;color:#fff;height:29px}
.flinks li:first-child{color:var(--green)}
.talk{left:421px;top:934px;font-size:21px;font-weight:700;color:var(--green)}
.talk small{display:block;font-size:10px;font-weight:400;margin-top:2px}
.dfield{left:423px;width:135px;height:21px;background:var(--field-dark);border-radius:2px;color:var(--green);font-size:8px;padding:6px 10px}
.send{left:420px;top:1146px;width:106px;height:24px;border-radius:12px;background:var(--green);color:#fff;font-size:7px;font-weight:700;text-align:center;line-height:24px}
.social{left:644px;font-size:10px;color:#fff;padding-left:30px;line-height:22px}
.social i{position:absolute;left:0;top:0;width:22px;height:22px;border-radius:3px;background:#8a8a88}
.social b{color:var(--green)}
.bottombar{left:0;top:1180px;width:862px;height:20px;background:var(--darker);font-size:8px;color:#fff}
.bottombar span{position:absolute;top:5px}
.bottombar u{color:var(--green)}
</style>
</head>
<body>
<div class="abs topbar"></div>
<i class="abs share" style="left:673px"></i><i class="abs share" style="left:700px"></i><i class="abs share" style="left:727px"></i><i class="abs share" style="left:754px"></i>

<header class="abs header"></header>
<div class="abs brand">pLirvo<i></i></div>
<nav class="abs nav">
  <a class="active">Why</a>
  <a style="left:112px">How It Works</a>
  <a style="left:202px">Sign Up</a>
  <a style="left:266px">Our Blog</a>
</nav>
<div class="login">
  <label style="left:498px;top:93px">Username</label>
  <div class="field" style="top:89px">member@plirvo.com</div>
  <label style="left:498px;top:115px">Password</label>
  <div class="field" style="top:112px">••••••••••</div>
  <div class="abs btn">Login</div>
</div>

<h1 class="abs"><span>Successful</span> Dating with<br>Professional Dating Advice!</h1>
<p class="abs lead">Amorilo offers members <span>unique access</span> to dating tips and <span>advice</span> from our professionals.</p>

<article class="abs post" style="top:336px"><div class="mark" style="background:var(--c-blue)">!</div><div class="meta">Posted by <b style="color:var(--c-blue)">Dale R</b> Tue Aug 16, 2011</div><p>Clipvault makes it easy for you to upload any kind of video you create. We accept tons of<br>formats. Basic (free) accounts allow for 500 MB of storage every week,</p></article>
<article class="abs post" style="top:398px"><div class="mark" style="background:var(--c-teal)">!</div><div class="meta">Posted by <b style="color:var(--c-teal)">kavren</b> Tue Aug 16, 2011</div><p>Clipvault makes it easy for you to upload any kind of video you create. We accept tons of different<br>file formats. Basic (free) accounts allow for 500 MB of storage every week,</p></article>
<article class="abs post" style="top:464px"><div class="mark" style="background:var(--c-purple)">!</div><div class="meta">Posted by <b style="color:var(--c-purple)">otto</b> Tue Aug 16, 2011</div><p>Clipvault makes it easy for you to upload any kind of video you create. We Basic (free) accounts<br>allow for 500 MB of storage every week,<br>formats.</p></article>
<article class="abs post" style="top:530px"><div class="mark" style="background:var(--c-orange)">!</div><div class="meta">Posted by <b style="color:var(--c-orange)">mikel</b> Tue Aug 16, 2011</div><p>Clipvault makes it easy for you to upload any kind of video you create. We accept tons of different file<br>formats. Basic (free) accounts allow for 500 MB of storage every week,</p></article>
<article class="abs post" style="top:594px"><div class="mark" style="background:var(--c-green)">!</div><div class="meta">Posted by <b style="color:var(--c-green)">Lena Brook</b> Tue Aug 16, 2011</div><p>Clipvault makes it easy for you to upload any kind of video you create. We accept<br>tons of different file formats.</p></article>

<section class="popular">
  <h2 class="abs">Most Popular On Love + Dating</h2>
  <ul class="abs">
    <li style="top:0"><span>A user asks: Does True And Unconditional Love Really,</span><small>Thu Oct 6, 2011 4:23 pm</small></li>
    <li style="top:41px"><span>20 Romantic Things to Say to a Woman</span><small>Tue Oct 11, 2011 7:42 am</small></li>
    <li style="top:75px"><span>Top 10 Real Reasons Men Break Up With Women</span><small>Tue Oct 11, 2011 7:29 am</small></li>
    <li style="top:109px"><span>User Post: I want a Hero!</span><small>Thu Oct 6, 2011 7:59am</small></li>
    <li style="top:145px"><span>Are All Guys Basically A-Holes? Sexpert Jenna Holt On the Surprising Truth</span><small>Tue Oct 11, 2011 1:39pm</small></li>
  </ul>
</section>

<h2 class="abs join">join today</h2>
<div class="abs input" style="top:370px">Name</div>
<div class="abs input" style="top:403px">Email</div>
<div class="abs input" style="top:435px">Comments</div>
<div class="abs signup">sign up</div>
<h2 class="abs why">Why <span>pLirvo</span> USA is<small>perfect for you...</small></h2>
<div class="abs feature" style="top:565px"><i style="background:var(--c-green)"></i>Find love, make friends and search for like-minded<br>people today!</div>
<div class="abs feature" style="top:595px"><i style="background:var(--c-purple)"></i>Find your ideal match with our intelligent two-way<br>matching system.</div>
<div class="abs feature" style="top:624px"><i style="background:var(--c-orange)"></i>Your personal details are kept safe and completely<br>private.</div>
<div class="abs cta">Sign Up Now</div>
<svg class="abs" style="left:579px;top:696px" width="56" height="56" viewBox="0 0 56 56" aria-label="Play video"><circle cx="28" cy="28" r="25" fill="#e4eef5" stroke="#7aaed0" stroke-width="3"/><path d="M21 15 L40 28 L21 41 Z" fill="#6aa6d2"/></svg>
<div class="abs video-label">Watch a Video</div>

<footer class="abs footer"></footer>
<div class="abs fbrand">pLirvo<i></i></div>
<div class="abs contact" style="top:982px"><svg width="22" height="16" viewBox="0 0 22 16"><path d="M1 5 Q11 -2 21 5 L18 8 L15 5 L7 5 L4 8 Z M5 9 L17 9 L19 15 L3 15 Z" fill="#111"/></svg><h3>Call Us</h3><p>150000 2 207</p></div>
<div class="abs contact" style="top:1034px"><svg width="20" height="15" viewBox="0 0 20 15"><rect x="1" y="1" width="18" height="13" fill="#111"/><path d="M1 1 L10 8 L19 1" stroke="#ddd" fill="none"/></svg><h3>Email Us</h3><p>info@plirvo.com</p></div>
<div class="abs contact" style="top:1086px"><svg width="18" height="20" viewBox="0 0 18 20"><rect x="1" y="1" width="16" height="18" rx="2" fill="#111" stroke="#888"/><rect x="5" y="5" width="8" height="8" fill="#666"/></svg><h3>Address</h3><p>2250 Marlow Ave.<br>San Francisco, CAxcs</p></div>
<ul class="abs flinks"><li>+ Why pLirvo</li><li>+ How it works</li><li>+ Sign Up</li><li>+ Login</li><li>+ About Us</li></ul>
<h2 class="abs talk">Let's Talk<small>drop us a message</small></h2>
<div class="abs dfield" style="top:983px">Name</div>
<div class="abs dfield" style="top:1012px">Email</div>
<div class="abs dfield" style="top:1041px;width:185px;height:98px">Comments</div>
<div class="abs send">SEND YOUR MESSAGE</div>
<div class="abs social" style="top:984px"><i></i>Become a <b>Chatterbook</b></div>
<div class="abs social" style="top:1012px"><i></i>Subscribe us <b>Circlo</b></div>
<div class="abs social" style="top:1041px"><i></i>Follow us <b>Yodel</b></div>
<div class="abs social" style="top:1069px"><i></i>Us on <b>Spacely</b></div>
<div class="abs social" style="top:1098px"><i></i>IDgate <b>Sign Up</b></div>
<div class="abs bottombar"><span style="left:100px">© Copyright 2011 pLirvo.com</span><span style="left:283px"><u>Privacy Policy</u> | Terms &amp; Conditions | Support</span></div>
</body>
</html>
```